Ridgely Forge business card for handing simple contact information and generating service awareness

Utilizing the attached logo(s), generate a professional, but approachable, card conveying a sense of capability and integrity. Please only use one logo of the four attached; the different colors are all acceptable, but preference will be given to a design integrating a teal/turquoise logo,

I do not know where to put in the contact information or details?

Target Market(s)

Agriculture, Farming, Timber, Forestry, Construction, Crane Service

Industry/Entity Type

Contact Information for Business Card

Name, Phone Number, email address

Colors

Designer to choose colors to be used in the design.

Requirements
Nice to have
• It would be great to have either a mountain or one of the attached cranes as a backdrop on the rear of the card. Simple watermarks and/or Debossing is also great

```html
<!DOCTYPE html>
<html lang="en">
<head>
<meta charset="utf-8">
<title>Ridgely Forge – Business Card</title>
<link rel="stylesheet" href="https://fonts.googleapis.com/css2?family=Open+Sans:wght@400;700;800&display=swap">
<style>
  :root {
    --bg: #3a3a3a;
    --card-dark: #1b1c1e;
    --brand-blue: #00aee2;
    --text-light: #f2f2f2;
    --white: #ffffff;
  }
  * { box-sizing: border-box; margin: 0; padding: 0; }
  html, body {
    width: 1200px;
    height: 780px;
    overflow: hidden;
    background: var(--bg);
    font-family: "Open Sans", Arial, sans-serif;
  }
  .canvas {
    width: 1200px;
    height: 780px;
    display: flex;
    align-items: center;
    justify-content: center;
    gap: 48px;
  }
  .card {
    width: 520px;
    height: 300px;
    border-radius: 22px;
    position: relative;
    overflow: hidden;
  }
  .card--front { background: var(--card-dark); }
  .card--back {
    background: var(--brand-blue);
    display: flex;
    align-items: center;
    justify-content: center;
  }

  .brand {
    display: flex;
    align-items: center;
    gap: 10px;
    font-weight: 800;
    text-transform: uppercase;
    letter-spacing: 0.5px;
    line-height: 1;
    white-space: nowrap;
  }
  .brand__dot {
    width: 18px;
    height: 18px;
    border-radius: 50%;
    flex: none;
  }
  .card--front .brand {
    position: absolute;
    left: 30px;
    top: 128px;
    font-size: 23px;
    color: var(--brand-blue);
  }
  .card--front .brand__dot { background: var(--brand-blue); }
  .card--back .brand { font-size: 40px; color: var(--white); }
  .card--back .brand__dot { width: 28px; height: 28px; background: var(--white); }

  .divider {
    position: absolute;
    left: 0; top: 0;
    width: 520px; height: 300px;
  }

  .contact {
    position: absolute;
    left: 322px;
    top: 58px;
    color: var(--text-light);
    white-space: nowrap;
  }
  .contact__name {
    color: var(--brand-blue);
    font-weight: 700;
    font-size: 24px;
    text-transform: uppercase;
    letter-spacing: 0.3px;
    line-height: 1.1;
  }
  .contact__role {
    font-size: 14px;
    margin-bottom: 14px;
  }
  .contact__list { list-style: none; }
  .contact__item {
    display: flex;
    align-items: center;
    gap: 8px;
    font-size: 14px;
    line-height: 1.7;
  }
  .contact__icon { width: 13px; height: 13px; flex: none; }
  .contact__address {
    font-size: 14px;
    line-height: 1.45;
    margin-top: 8px;
  }
</style>
</head>
<body>
<main class="canvas">
  <section class="card card--front">
    <div class="brand"><span class="brand__dot"></span>Ridgely Forge</div>

    <svg class="divider" viewBox="0 0 520 300" aria-hidden="true">
      <line x1="264" y1="270" x2="308" y2="30" stroke="#00aee2" stroke-width="1.5"/>
    </svg>

    <div class="contact">
      <h1 class="contact__name">Owen Hale</h1>
      <p class="contact__role">Managing Director</p>
      <ul class="contact__list">
        <li class="contact__item">
          <svg class="contact__icon" viewBox="0 0 16 16" aria-hidden="true"><path fill="#00aee2" d="M3.5 1.5l2.5 0 1 3.5-1.8 1.2a8 8 0 0 0 4.6 4.6L11 9l3.5 1v2.5A2 2 0 0 1 12.5 14.5 11 11 0 0 1 1.5 3.5 2 2 0 0 1 3.5 1.5z"/></svg>
          123 456 789
        </li>
        <li class="contact__item">
          <svg class="contact__icon" viewBox="0 0 16 16" aria-hidden="true"><rect x="1" y="3" width="14" height="10" rx="1.5" fill="#00aee2"/><path d="M1.5 4l6.5 5 6.5-5" fill="none" stroke="#1b1c1e" stroke-width="1.3"/></svg>
          info@yourgmail.com
        </li>
        <li class="contact__item">
          <svg class="contact__icon" viewBox="0 0 16 16" aria-hidden="true"><circle cx="8" cy="8" r="7" fill="#00aee2"/><path d="M1 8h14M8 1c-3 3.5-3 10.5 0 14M8 1c3 3.5 3 10.5 0 14" fill="none" stroke="#1b1c1e" stroke-width="1"/></svg>
          www.yourwebsite.com
        </li>
      </ul>
      <p class="contact__address">Your address, City<br>State, Zip 1234</p>
    </div>
  </section>

  <section class="card card--back">
    <div class="brand"><span class="brand__dot"></span>Ridgely Forge</div>
  </section>
</main>
</body>
</html>
```